TV+Music+Social Network+Entertainment+yellowpages= Designers lol

TV+ Music+ Social Network +Entertainment+ yellowpages=

ZAVQUEL.COM

Zavquel is a one-stop shop promotional plateform that will communicate information to all user of what is COOL, NEW and Exicting in your Neighborhood.(News,Events,Entertainment,ect) We promote for all User/Entrepreneur/business/Talents.We are the future and dream destination for all to whom owns a computer. Forming the the World Wide Web into your Local Wide Web. (Atlanta, Dallas, Las Vegas, New York ect.)

* EX: ( WWW. ??? .com =LWW. ??? .com)
WORLD = LOCAL

* Goal/Mission: Have customer/user visit the website and then leave their house to go experience life in their respective surroundings.

/////////////////////////Web page///////////////////////

Colors:Blue/Green/black

include: interchangable background picture @ top (to update easily and keep fresh) On this background picture include logo (top left) login/sign (top left)

Major Tabs: Music/Daylife/Nightlife/Video/Shop

• Tv screen/search engine

```html
<!DOCTYPE html>
<html lang="en">
<head>
<meta charset="utf-8">
<title>Zavquel – Night Life</title>
<link rel="stylesheet" href="https://fonts.googleapis.com/css2?family=Cinzel:wght@400;700&family=Marcellus&family=Open+Sans:wght@400;600&display=swap">
<style>
  :root {
    --night-deep: #0b0d12;
    --night-mid: #3a3d45;
    --haze: #f4f5f7;
    --blue-core: #0a2fb8;
    --blue-dark: #00092e;
    --blue-light: #b8c4f0;
    --blue-link: #1560e0;
    --silver: #dfe3ec;
    --menu-text: #a9abb3;
    --panel-white: #ffffff;
    --share-red: #e00000;
  }
  * { box-sizing: border-box; margin: 0; padding: 0; }
  html, body { width: 1200px; height: 900px; overflow: hidden; }
  body { position: relative; font-family: "Marcellus", serif; background: var(--haze); }

  .city-backdrop {
    position: absolute; inset: 0;
    background:
      linear-gradient(180deg, rgba(11,13,18,0.95) 0%, rgba(40,43,50,0.9) 30%, rgba(110,112,118,0.7) 58%, rgba(235,236,238,0.95) 82%, var(--haze) 100%);
  }

  .brand {
    position: absolute; left: 35px; top: 28px;
    display: flex; align-items: center; gap: 10px;
    font-family: "Open Sans", sans-serif; font-weight: 600; font-size: 26px; color: #ffffff;
  }
  .brand-dot { width: 34px; height: 34px; border-radius: 50%; background: var(--blue-link); }

  .sign-in {
    position: absolute; left: 1017px; top: 14px;
    font-family: "Marcellus", serif; font-size: 18px; color: var(--blue-link); text-decoration: none;
  }

  .home-button {
    position: absolute; left: 51px; top: 94px; width: 70px; height: 70px;
  }

  .page-title {
    position: absolute; left: 158px; top: 66px; width: 900px; height: 120px;
    display: flex; justify-content: space-between; align-items: center;
    font-family: "Cinzel", serif; font-weight: 700; font-size: 130px; line-height: 1;
    color: var(--blue-dark);
    -webkit-text-stroke: 2px #1d5cff;
    text-shadow: 0 0 12px rgba(40,110,255,0.7), 3px 4px 4px rgba(0,0,0,0.8);
  }

  .side-menu {
    position: absolute; left: 18px; top: 214px; width: 133px; height: 653px;
    border-radius: 8px; overflow: hidden;
    background: linear-gradient(90deg, var(--blue-dark) 0%, var(--blue-core) 50%, var(--blue-dark) 100%);
    display: flex; flex-direction: column;
    box-shadow: 0 0 6px rgba(0,0,0,0.6);
  }
  .side-menu a {
    flex: 1; display: flex; align-items: center; justify-content: center; text-align: center;
    color: var(--menu-text); font-size: 26px; line-height: 1.3; text-decoration: none;
    border-bottom: 3px solid rgba(0,0,0,0.55);
  }
  .side-menu a:last-child { border-bottom: none; }
  .side-menu .city-tab {
    flex: 0 0 78px; margin: 4px; border-radius: 6px; font-size: 23px;
    background: linear-gradient(180deg, #6b6b6b 0%, #111 30%, #000 100%);
    border-bottom: none;
  }

  .content-panel {
    position: absolute; left: 190px; top: 265px; width: 936px; height: 515px;
    border-radius: 10px;
    background: linear-gradient(180deg, #2a2a2a 0%, #8a8a8a 6%, #e8e8e8 13%, var(--panel-white) 20%, var(--panel-white) 80%, #d5d5d5 100%);
    box-shadow: 0 0 10px rgba(0,0,0,0.4);
  }
  .content-panel::before {
    content: ""; position: absolute; inset: 30px 20px 20px 20px;
    background: var(--panel-white); border-radius: 4px;
    box-shadow: 0 0 30px 20px var(--panel-white);
  }

  .section-tile {
    position: absolute; width: 214px; height: 149px;
    border: 1px solid #000;
    background:
      radial-gradient(ellipse 45% 22% at 50% 18%, var(--blue-light) 0%, rgba(184,196,240,0.4) 70%, transparent 100%),
      linear-gradient(180deg, #2f55e0 0%, var(--blue-core) 45%, #00166e 75%, var(--blue-dark) 100%);
    box-shadow: 2px 3px 5px rgba(0,0,0,0.5);
    display: flex; align-items: center; justify-content: center;
    text-decoration: none;
  }
  .section-tile span {
    font-family: "Marcellus", serif;
    background: linear-gradient(180deg, #ffffff 0%, var(--silver) 50%, #8d93a4 100%);
    -webkit-background-clip: text; background-clip: text; color: transparent;
    filter: drop-shadow(1px 2px 1px rgba(0,0,0,0.6));
    line-height: 1;
  }

  .social-links {
    position: absolute; top: 791px; left: 0; width: 1200px; height: 70px;
  }
  .social-item {
    position: absolute; display: flex; flex-direction: column; align-items: center; gap: 4px;
    font-family: "Marcellus", serif; font-size: 14px; color: #1a1d2a; text-decoration: none;
  }
  .social-square { width: 44px; height: 44px; background: #2a2f3c; border-radius: 4px; }
  .share-button {
    position: absolute; left: 757px; top: 799px; width: 114px; height: 54px;
    border-radius: 8px; border: 1px solid #600;
    background: linear-gradient(180deg, #ff4a4a 0%, var(--share-red) 45%, #a00000 100%);
    box-shadow: 2px 4px 5px rgba(0,0,0,0.45);
    display: flex; align-items: center; justify-content: center;
    font-family: "Open Sans", sans-serif; font-size: 24px; color: #000; text-decoration: none;
  }
</style>
</head>
<body>
  <div class="city-backdrop" role="img" aria-label="Night skyline of New York with searchlight beams, fading to white at the bottom"></div>

  <div class="brand"><span class="brand-dot"></span>Zavquel</div>
  <a class="sign-in" href="#">Sign in/Register</a>

  <svg class="home-button" viewBox="0 0 70 70" aria-label="Home">
    <defs>
      <radialGradient id="homeGlow" cx="40%" cy="30%" r="70%">
        <stop offset="0" stop-color="#6f8cff"/>
        <stop offset="0.5" stop-color="#1436d8"/>
        <stop offset="1" stop-color="#020a40"/>
      </radialGradient>
    </defs>
    <circle cx="35" cy="35" r="34" fill="url(#homeGlow)" stroke="#0a1a7a" stroke-width="2"/>
    <path d="M35 18 L16 35 H22 V51 H31 V41 H39 V51 H48 V35 H54 Z" fill="#000"/>
  </svg>

  <h1 class="page-title" aria-label="Night Life">
    <span>N</span><span>I</span><span>G</span><span>H</span><span>T</span><span>&nbsp;</span><span>L</span><span>I</span><span>F</span><span>E</span>
  </h1>

  <nav class="side-menu">
    <a class="city-tab" href="#">New York</a>
    <a href="#">Whos<br>out now</a>
    <a href="#">Hot<br>Spots</a>
    <a href="#">Fine<br>Dining</a>
    <a href="#">General<br>Outing</a>
    <a href="#">Clubbing<br>&amp;<br>Noise</a>
    <a href="#">Meet<br>Someone</a>
  </nav>

  <div class="content-panel"></div>

  <a class="section-tile" href="#" style="left:302px;top:354px"><span style="font-size:54px">Photos</span></a>
  <a class="section-tile" href="#" style="left:533px;top:354px"><span style="font-size:54px">Videos</span></a>
  <a class="section-tile" href="#" style="left:763px;top:354px"><span style="font-size:68px">Clubs</span></a>
  <a class="section-tile" href="#" style="left:302px;top:510px"><span style="font-size:80px">Live</span></a>
  <a class="section-tile" href="#" style="left:533px;top:510px"><span style="font-size:66px">Food</span></a>
  <a class="section-tile" href="#" style="left:763px;top:510px"><span style="font-size:50px">Connect</span></a>

  <div class="social-links">
    <a class="social-item" href="#" style="left:370px"><span class="social-square"></span>Friendlio</a>
    <a class="social-item" href="#" style="left:510px"><span class="social-square"></span>Chirply</a>
    <a class="social-item" href="#" style="left:635px"><span class="social-square"></span>Gathera</a>
  </div>
  <a class="share-button" href="#">Share +</a>
</body>
</html>
```